Stationary design for boutique production house

We need a stationary design for our production house, 'Lorin Studios' based in Singapore. We produce microfilms as well as podcasts, talkshows and events. Our logo is a stylized icon of our director, who is also the executive producer and host of our programs, Lorin. Our main company colors are Red, Black and white. We would like a clean, minimalist design incorporating our existing company logo that conveys a sense of urbanism and elegance.

Logo and font files are attached. f

Target Market(s)

We focus on lifestyle media rather than entertainment.

Industry/Entity Type

Boutique

Font styles to use
Serif
Sans Serif

Colors
ec1f27
ffffff
000000

Requirements
Must have
• Our company logo and at least one of our company colors.
Nice to have
• Our address and contact information.
Should not have
• Changes made to the company logo (using only certain parts of it is fine though)

```html
<!DOCTYPE html>
<html lang="en">
<head>
<meta charset="utf-8">
<title>Lorin Studios — Stationery</title>
<link href="https://fonts.googleapis.com/css2?family=Libre+Baskerville:wght@700&family=Open+Sans:wght@400;600&display=swap" rel="stylesheet">
<style>
:root{
  --red:#ec1f27;
  --red-deep:#c8141b;
  --black:#000000;
  --white:#ffffff;
  --ink:#555555;
  --ground:#e4e4e4;
  --serif:"Libre Baskerville", "Times New Roman", serif;
  --sans:"Open Sans", Arial, sans-serif;
}
*{box-sizing:border-box;margin:0;padding:0}
html,body{width:1200px;height:900px;overflow:hidden;background:var(--ground)}
.canvas{position:relative;width:1200px;height:900px}

.wordmark{font-family:var(--serif);font-weight:700;text-transform:uppercase;letter-spacing:.04em;line-height:1.15;text-align:center}
.wordmark-dot{display:block;border-radius:50%;margin:0 auto}

/* Notebook cover */
.notebook{position:absolute;left:50px;top:40px;width:330px;height:450px;background:var(--red);border-radius:4px 10px 10px 4px}
.notebook .wordmark{position:absolute;left:0;right:50px;top:170px;font-size:30px;color:var(--red-deep)}
.notebook .wordmark-dot{width:22px;height:22px;background:var(--red-deep);margin-bottom:14px}
.notebook-band{position:absolute;top:0;bottom:0;right:36px;width:7px;background:#1a1a1a}

/* Business cards */
.card{position:absolute;top:540px;width:170px;height:270px;border-radius:3px;box-shadow:0 0 0 1px rgba(0,0,0,.05)}
.card-red{left:50px;background:var(--red)}
.card-red .wordmark{color:var(--white)}
.card-red .wordmark-dot{background:var(--white)}
.card-white{left:240px;background:var(--white);border-bottom:4px solid var(--red)}
.card-white .wordmark{color:var(--black)}
.card-white .wordmark-dot{background:var(--red)}
.card .wordmark{position:absolute;left:0;right:0;top:90px;font-size:17px}
.card .wordmark-dot{width:14px;height:14px;margin-bottom:10px}
.card-contact{left:430px;background:var(--white);border-bottom:4px solid var(--red)}
.card-contact .wordmark{position:absolute;left:0;right:0;top:32px;font-size:13px;color:var(--black)}
.card-contact .wordmark-dot{width:10px;height:10px;background:var(--red);margin-bottom:8px}
.contact-block{position:absolute;left:0;right:0;top:128px;text-align:center;font-family:var(--serif);font-size:9px;line-height:1.55;color:var(--black)}
.contact-name{color:var(--red);font-size:11px;letter-spacing:.05em}
.contact-title{margin-bottom:4px}
.contact-rule{width:110px;height:1px;background:var(--red);margin:5px auto}
.contact-web{color:var(--red)}

/* Letterhead */
.letterhead{position:absolute;left:640px;top:40px;width:520px;height:735px;background:var(--white);box-shadow:0 1px 3px rgba(0,0,0,.08)}
.letterhead-mark{position:absolute;left:36px;top:0;width:110px;height:110px;background:var(--red);display:flex;flex-direction:column;justify-content:center}
.letterhead-mark .wordmark{color:var(--white);font-size:12px}
.letterhead-mark .wordmark-dot{width:10px;height:10px;background:var(--white);margin-bottom:8px}
.letter{position:absolute;left:60px;right:50px;top:180px;font-family:var(--sans);font-size:10.5px;line-height:1.6;color:var(--ink)}
.letter-sender{font-size:12px}
.letter-date{margin-bottom:16px}
.letter p{margin-bottom:14px}
.letterhead-contact{position:absolute;left:36px;bottom:0;width:110px;height:110px;background:var(--red);color:var(--white);font-family:var(--serif);font-size:7.5px;line-height:1.5;padding:14px 8px 0;text-align:center}
.pin{display:block;margin:0 auto 6px}
.approval-stamp{position:absolute;right:70px;bottom:60px;width:70px;height:70px;border-radius:50%;border:2px solid #9a95c0;opacity:.6}
</style>
</head>
<body>
<main class="canvas">

  <section class="notebook" aria-label="Notebook cover">
    <div class="wordmark"><span class="wordmark-dot"></span>Lorin<br>Studios</div>
    <div class="notebook-band"></div>
  </section>

  <section class="card card-red" aria-label="Business card, red front">
    <div class="wordmark"><span class="wordmark-dot"></span>Lorin<br>Studios</div>
  </section>

  <section class="card card-white" aria-label="Business card, white front">
    <div class="wordmark"><span class="wordmark-dot"></span>Lorin<br>Studios</div>
  </section>

  <section class="card card-contact" aria-label="Business card, contact side">
    <div class="wordmark"><span class="wordmark-dot"></span>Lorin<br>Studios</div>
    <div class="contact-block">
      <div class="contact-name">LORIN HALE</div>
      <div class="contact-title">President</div>
      <div class="contact-rule"></div>
      <div>Street Address Line 1</div>
      <div>Your City, Postal Code</div>
      <div>T: 00 (0)00 0000</div>
      <div>F: 00 (0)00 0000</div>
      <div>E: info@lorinstudios.com</div>
      <div class="contact-web">www.lorinstudios.com</div>
      <div class="contact-rule"></div>
    </div>
  </section>

  <section class="letterhead" aria-label="Letterhead">
    <div class="letterhead-mark">
      <div class="wordmark"><span class="wordmark-dot"></span>Lorin<br>Studios</div>
    </div>
    <article class="letter">
      <div class="letter-sender">Lorin Studios</div>
      <div class="letter-date">December 22, 2014/Revised February 2, 2015</div>
      <p>Thank you for joining us at our recent studio session. This note confirms the schedule, the crew list and the shoot locations we discussed, along with the budget notes for the coming month.</p>
      <p>Our team will prepare the set, lighting and sound on the morning of the first day. Please send any script changes a week ahead so that rehearsals can run smoothly and on time.</p>
      <p>We look forward to working with you again and to sharing the finished film with your audience.</p>
    </article>
    <div class="letterhead-contact">
      <svg class="pin" width="12" height="14" viewBox="0 0 12 14" aria-hidden="true">
        <path d="M6 0a5 5 0 0 0-5 5c0 3.6 5 9 5 9s5-5.4 5-9a5 5 0 0 0-5-5z" fill="#ffffff"/>
        <circle cx="6" cy="5" r="2" fill="#ec1f27"/>
      </svg>
      Street Address Line 1<br>
      Your City, Postal Code<br>
      T: 00 (0)00 0000<br>
      F: 00 (0)00 0000<br>
      info@lorinstudios.com<br>
      www.lorinstudios.com
    </div>
    <div class="approval-stamp" role="img" aria-label="Approval stamp"></div>
  </section>

</main>
</body>
</html>
```